Taomeng business card -we import and distributed Chinese herbal medicine into Australia for prac...

We need a business card for our recently purchased and rebranded company. We are a small family run business - husband and wife team. Our logo is red and black, and we would like the card to be white, with an element of gold in the design (the first cloud in the attached png) which when printed we would like embossed in gold. Our website uses Chinese water colour paintings in the banners (www.taomeng.net.au) so a design that is in harmony with this would be ideal.
side one needs to include:

Target Market(s)

potential customers

Industry/Entity Type

Health And Wellness

Contact Information for Business Card

Side 1
logo,
Edmund Varsk Director
Practitioner Support and Education
0491 722 413
edmund@taomeng.net.au
218 Colbury St, Harrowby, WA, 6098

side 2 needs to include:
logo
Priscilla Moult Director
Orders, Accounts and Despatch
0487 530 619
priscilla@taomeng.net.au

Font styles to use
Serif

Colors

Designer to choose colors to be used in the design.

Requirements
Must have
• black, red, gold colours
Nice to have
• we like the font papyrus (mac font)

```html
<!DOCTYPE html>
<html lang="en">
<head>
<meta charset="utf-8">
<title>Taomeng business cards</title>
<link href="https://fonts.googleapis.com/css2?family=Macondo&display=swap" rel="stylesheet">
<style>
  :root {
    --page-bg: #d8eff9;
    --ink: #1c2340;
    --seal-red: #e0351f;
    --band: #cfdde8;
    --wash-light: #f4fbfb;
    --wash-mid: #d3eeee;
    --wash-deep: #bfe5e8;
  }
  * { box-sizing: border-box; margin: 0; padding: 0; }
  html, body {
    width: 1200px; height: 1200px; overflow: hidden;
    background: var(--page-bg);
  }
  body { position: relative; font-family: "Macondo", serif; color: var(--ink); }

  .card {
    position: absolute; left: 212px; width: 766px; height: 437px;
    overflow: hidden;
  }
  .card--front { top: 85px; }
  .card--back { top: 661px; }

  .card__wash {
    position: absolute; inset: 0;
    background:
      radial-gradient(ellipse 45% 60% at 25% 40%, var(--wash-deep), transparent 70%),
      radial-gradient(ellipse 40% 50% at 70% 20%, var(--wash-mid), transparent 70%),
      radial-gradient(ellipse 60% 40% at 20% 95%, var(--wash-mid), transparent 70%),
      var(--wash-light);
  }

  .brand {
    position: absolute; top: 128px; left: 0; right: 0;
    display: flex; justify-content: center; align-items: center; gap: 14px;
  }
  .brand__square { width: 26px; height: 26px; background: var(--seal-red); }
  .brand__name { font-size: 44px; line-height: 1; color: var(--ink); }

  .person {
    position: absolute; top: 222px; left: 0; right: 0; text-align: center;
  }
  .person__name { font-size: 38px; line-height: 1.1; }
  .person__role { font-size: 22px; margin-top: 6px; line-height: 1.1; }

  .contact-band {
    position: absolute; top: 366px; left: 0; right: 0; height: 28px;
    background: var(--band);
    display: flex; align-items: center; justify-content: space-between;
    padding: 0 30px;
    font-size: 17px;
  }
  .contact-item { display: flex; align-items: center; gap: 8px; white-space: nowrap; }
  .contact-item svg { width: 17px; height: 17px; fill: var(--ink); flex: none; }
</style>
</head>
<body>

<section class="card card--front">
  <div class="card__wash" role="img" aria-label="Soft blue-green Chinese watercolour wash background"></div>
  <div class="brand"><span class="brand__square"></span><span class="brand__name">Taomeng</span></div>
  <div class="person">
    <p class="person__name">Edmund Varsk Director</p>
    <p class="person__role">Practitioner support and Education</p>
  </div>
  <div class="contact-band">
    <span class="contact-item">
      <svg viewBox="0 0 24 24"><path d="M6.6 10.8a15.1 15.1 0 0 0 6.6 6.6l2.2-2.2a1 1 0 0 1 1-.25 11.4 11.4 0 0 0 3.6.57 1 1 0 0 1 1 1V20a1 1 0 0 1-1 1A17 17 0 0 1 3 4a1 1 0 0 1 1-1h3.5a1 1 0 0 1 1 1c0 1.25.2 2.45.57 3.57a1 1 0 0 1-.25 1z"/></svg>
      0491 722 413
    </span>
    <span class="contact-item">
      <svg viewBox="0 0 24 24"><path d="M2 5h20v14H2z M3.5 6.5 12 13l8.5-6.5" fill="none" stroke="#1c2340" stroke-width="2"/><path d="M2 5h20L12 13z"/></svg>
      edmund@taomeng.net.au
    </span>
    <span class="contact-item">
      <svg viewBox="0 0 24 24"><path d="M12 2a7 7 0 0 0-7 7c0 5.2 7 13 7 13s7-7.8 7-13a7 7 0 0 0-7-7zm0 9.5A2.5 2.5 0 1 1 12 6.5a2.5 2.5 0 0 1 0 5z"/></svg>
      218 Colbury St, Harrowby, WA, 6098
    </span>
  </div>
</section>

<section class="card card--back">
  <div class="card__wash" role="img" aria-label="Soft blue-green Chinese watercolour wash background"></div>
  <div class="brand"><span class="brand__square"></span><span class="brand__name">Taomeng</span></div>
  <div class="person">
    <p class="person__name">Priscilla Moult Director</p>
    <p class="person__role">Orders, Accounts and Despatch</p>
  </div>
  <div class="contact-band">
    <span class="contact-item">
      <svg viewBox="0 0 24 24"><path d="M6.6 10.8a15.1 15.1 0 0 0 6.6 6.6l2.2-2.2a1 1 0 0 1 1-.25 11.4 11.4 0 0 0 3.6.57 1 1 0 0 1 1 1V20a1 1 0 0 1-1 1A17 17 0 0 1 3 4a1 1 0 0 1 1-1h3.5a1 1 0 0 1 1 1c0 1.25.2 2.45.57 3.57a1 1 0 0 1-.25 1z"/></svg>
      0487 530 619
    </span>
    <span class="contact-item">
      <svg viewBox="0 0 24 24"><path d="M2 5h20v14H2z M3.5 6.5 12 13l8.5-6.5" fill="none" stroke="#1c2340" stroke-width="2"/><path d="M2 5h20L12 13z"/></svg>
      priscilla@taomeng.net.au
    </span>
    <span class="contact-item">
      <svg viewBox="0 0 24 24"><path d="M12 2a7 7 0 0 0-7 7c0 5.2 7 13 7 13s7-7.8 7-13a7 7 0 0 0-7-7zm0 9.5A2.5 2.5 0 1 1 12 6.5a2.5 2.5 0 0 1 0 5z"/></svg>
      218 Colbury St, Harrowby, WA, 6098
    </span>
  </div>
</section>

</body>
</html>
```